Business Card and Stationary Design

After the successful redesign of our logo we are wanting to follow suite and create a new business card and stationary design!

New Logo is attached, information required on the business card should contain a mixture of the following but layout/arrangement is up to the designer.

Happy if the national provider number and abn are on the back, and happy for them to be smaller than the rest.

I am also happy to receive single sided or weird and wonderful designs.

Name
Title
National Provider Number 7291
ABN 53 219 864 317
Level 3, 42 Marlow Street
Brackenridge NSW 2291
Ph: 1300 987 214
Mobile: 0432 785 619
name@ferngatebuild.com.au
www.ferngatebuild.com.au

Target Market(s)

Professionals, Peers, Students, Suppliers...

Industry/Entity Type

Construction

Contact Information for Business Card

Listed in project description

Font styles to use
Other font styles liked:
• Century Gothic

Colors
0455a3
3176b5
ffffff

Requirements
Must have
• Professional Design, same color scheme as our logo
Nice to have
• Something that sets our apart from everyone else would be fantastic, open to size and shape and layout options, as long as they present professionally.
• Open to raised/embossed text, alternative materials, custom sizes, clear material
Should not have
• The color orange

```html
<!DOCTYPE html>
<html lang="en">
<head>
<meta charset="utf-8">
<title>Ferngate Build – Business Card</title>
<link href="https://fonts.googleapis.com/css2?family=Questrial&family=Montserrat:wght@700&display=swap" rel="stylesheet">
<style>
  :root {
    --stage: #d6d6d8;
    --brand-blue: #1d3579;
    --brand-blue-light: #2b4a8f;
    --white: #ffffff;
    --muted-grey: #8a8d95;
    --pattern-tint: #e7eaf1;
    --pattern-grey: #f1f1f1;
  }
  * { margin: 0; padding: 0; box-sizing: border-box; }
  html, body { width: 1200px; height: 1000px; overflow: hidden; }
  body {
    background: var(--stage);
    font-family: "Questrial", "Century Gothic", sans-serif;
    color: var(--white);
    position: relative;
  }
  .card {
    position: absolute;
    left: 269px;
    width: 662px;
    height: 379px;
    box-shadow: 0 3px 8px rgba(0,0,0,0.35);
    overflow: hidden;
  }
  .card-front {
    top: 108px;
    background: linear-gradient(120deg, var(--brand-blue) 35%, var(--brand-blue-light) 70%, var(--brand-blue) 100%);
  }
  .brand-lockup {
    position: absolute;
    left: 80px;
    top: 140px;
    display: flex;
    align-items: center;
    gap: 18px;
  }
  .brand-square {
    width: 58px;
    height: 58px;
    background: var(--white);
  }
  .brand-name {
    font-size: 54px;
    line-height: 1;
    color: var(--white);
  }
  .brand-tagline {
    position: absolute;
    left: 190px;
    top: 216px;
    font-size: 15px;
    letter-spacing: 1px;
    color: var(--muted-grey);
  }
  .front-web {
    position: absolute;
    left: 0;
    right: 0;
    top: 332px;
    text-align: center;
    font-size: 16px;
    letter-spacing: 0.3px;
  }
  .card-back {
    top: 521px;
    background: var(--white);
  }
  .back-decoration {
    position: absolute;
    left: 0;
    top: 0;
    width: 351px;
    height: 379px;
    background: linear-gradient(90deg, var(--pattern-tint) 0%, var(--pattern-tint) 72%, var(--pattern-grey) 100%);
  }
  .contact-panel {
    position: absolute;
    left: 351px;
    top: 0;
    width: 311px;
    height: 379px;
    background: linear-gradient(120deg, var(--brand-blue) 30%, var(--brand-blue-light) 75%);
    padding: 74px 0 0 34px;
    font-size: 15.5px;
    line-height: 19px;
  }
  .person-name {
    font-family: "Montserrat", "Century Gothic", sans-serif;
    font-weight: 700;
    font-size: 17px;
    letter-spacing: 0.3px;
  }
  .person-title { color: var(--muted-grey); margin-top: 2px; }
  .address { margin-top: 17px; }
  .contact-list { list-style: none; margin-top: 11px; }
  .contact-list li { display: flex; align-items: center; gap: 5px; }
  .contact-list svg { width: 11px; height: 11px; flex: none; }
  .registration { margin-top: 12px; }
</style>
</head>
<body>
  <section class="card card-front">
    <div class="brand-lockup">
      <span class="brand-square"></span>
      <span class="brand-name">ferngate build</span>
    </div>
    <p class="brand-tagline">DESIGN • CONSTRUCTION • PROJECTS • SUPPORT</p>
    <p class="front-web">www.ferngatebuild.com.au</p>
  </section>

  <section class="card card-back">
    <div class="back-decoration" role="img" aria-label="Large faint brand symbol decoration in pale blue-grey"></div>
    <div class="contact-panel">
      <p class="person-name">DANIEL HARPER</p>
      <p class="person-title">Managing Director</p>
      <p class="address">Level 3, 42 Marlow Street<br>Brackenridge NSW 2291</p>
      <ul class="contact-list">
        <li><svg viewBox="0 0 12 12" aria-hidden="true"><path d="M3 1 L5 3.5 L4 5 Q5.5 7 7 8 L8.5 7 L11 9 L9.5 11 Q4 10 1 2.5 Z" fill="#9aa3b8"/></svg>1300 987 214</li>
        <li><svg viewBox="0 0 12 12" aria-hidden="true"><rect x="3" y="0.5" width="6" height="11" rx="1" fill="none" stroke="#9aa3b8" stroke-width="1.2"/></svg>0432 785 619</li>
        <li><svg viewBox="0 0 12 12" aria-hidden="true"><rect x="0.5" y="2.5" width="11" height="7" fill="#9aa3b8"/><path d="M0.5 2.5 L6 7 L11.5 2.5" fill="none" stroke="#1d3579" stroke-width="1"/></svg>name@ferngatebuild.com.au</li>
        <li><svg viewBox="0 0 12 12" aria-hidden="true"><circle cx="6" cy="6" r="5.3" fill="none" stroke="#9aa3b8" stroke-width="1.2"/><path d="M0.7 6 H11.3 M6 0.7 V11.3" stroke="#9aa3b8" stroke-width="1"/></svg>www.ferngatebuild.com.au</li>
      </ul>
      <p class="registration">National Provider Number: 7291<br>ABN: 53 219 864 317</p>
    </div>
  </section>
</body>
</html>
```